Surgery Office Letterhead Design

I'm seeking new letterhead that will comprise all of our office locations and logo and other applicable information, per the following:

Office Locations:

Lakemont Institute for Jaw & Face Surgery at Cleburne
347 Hazelpine Court
Marlow Springs, Texas 75921
Phone 555.382.4706
Fax 555.382.9034

Lakemont Institute for Jaw & Face Surgery at Stephenville
518 Willowgate Boulevard
Pinecrest, Texas 75938
Phone 555.563.2781
Fax 555.563.2789

Lakemont Institute for Jaw & Face Surgery at Belton
739 West 9th Avenue
Cedar Bend, Texas 75964
Phone 555.871.4035
Fax 555.871.4042

Other Info to include:

www.lakemontjawface.com
hello@lakemontjawface.com

Industry/Entity Type

Medical

Font styles to use
Serif
Sans Serif

Requirements
Must have
• See Project Description

```html
<!DOCTYPE html>
<html lang="en">
<head>
<meta charset="utf-8">
<title>Lakemont Institute Letterhead</title>
<link rel="stylesheet" href="https://fonts.googleapis.com/css2?family=Libre+Baskerville&family=Questrial&display=swap">
<style>
  :root {
    --backdrop: #d9d9db;
    --paper: #f6f6f6;
    --navy: #2f4470;
    --ink: #4d4d52;
    --rule: #b9b9bd;
  }
  * { margin: 0; padding: 0; box-sizing: border-box; }
  html, body { width: 1200px; height: 1069px; overflow: hidden; background: var(--backdrop); }
  .letterhead {
    position: absolute; left: 202px; top: 20px;
    width: 795px; height: 1029px;
    background: var(--paper);
    box-shadow: 0 2px 6px rgba(0,0,0,.18);
  }
  .brand {
    position: absolute; left: 59px; top: 100px;
    display: flex; align-items: center; gap: 9px;
  }
  .brand-dot { width: 11px; height: 11px; border-radius: 50%; background: var(--navy); }
  .brand-name {
    font-family: "Libre Baskerville", serif;
    font-size: 17px; color: var(--navy); letter-spacing: .3px; white-space: nowrap;
  }
  .footer {
    position: absolute; left: 0; top: 937px; width: 100%;
    font-family: "Questrial", sans-serif; font-size: 10.5px; line-height: 12.4px;
    color: var(--ink);
  }
  .office { position: absolute; top: 0; white-space: nowrap; }
  .office h2 {
    font-family: "Questrial", sans-serif;
    font-size: 10px; line-height: 12.4px; font-weight: 700; color: var(--navy);
    text-transform: uppercase; letter-spacing: 0;
  }
  .divider { position: absolute; top: 1px; width: 1px; height: 58px; background: var(--rule); }
</style>
</head>
<body>
  <main class="letterhead">
    <header class="brand">
      <span class="brand-dot"></span>
      <span class="brand-name">LAKEMONT INSTITUTE</span>
    </header>

    <footer class="footer">
      <section class="office" style="left:59px">
        <h2>Lakemont Institute<br>for Jaw &amp; Face Surgery</h2>
        <p>hello@lakemontjawface.com<br>www.lakemontjawface.com</p>
      </section>
      <span class="divider" style="left:240px"></span>
      <section class="office" style="left:269px">
        <h2>Marlow Springs</h2>
        <p>347 Hazelpine Court<br>Marlow Springs, Texas 75921<br>Phone 555.382.4706<br>Fax 555.382.9034</p>
      </section>
      <span class="divider" style="left:413px"></span>
      <section class="office" style="left:443px">
        <h2>Pinecrest</h2>
        <p>518 Willowgate Boulevard<br>Pinecrest, Texas 75938<br>Phone 555.563.2781<br>Fax 555.563.2789</p>
      </section>
      <span class="divider" style="left:603px"></span>
      <section class="office" style="left:634px">
        <h2>Cedar Bend</h2>
        <p>739 West 9th Avenue<br>Cedar Bend, Texas 75964<br>Phone 555.871.4035<br>Fax 555.871.4042</p>
      </section>
    </footer>
  </main>
</body>
</html>
```